732RidgeWorks varden moto halvex van wrap

Have a 2020 varden moto halvex that I want to do a full van wrap on. I have another van already wrapped that i would like to kinda play off of with the color schemes.

```html
<!DOCTYPE html>
<html lang="en">
<head>
<meta charset="utf-8">
<title>732RidgeWorks varden moto halvex van wrap</title>
<link rel="stylesheet" href="https://fonts.googleapis.com/css2?family=Montserrat:wght@600;700&display=swap">
<style>
  :root {
    --wrap-blue: #3a78c2;
    --wrap-blue-deep: #2f6bb3;
    --wrap-green: #8cc63f;
    --wrap-orange: #e98d27;
    --wrap-white: #f7f7f7;
    --trim-black: #1f1f1f;
    --glass: #4a4a4a;
    --glass-light: #c9c9c9;
    --hub: #b9bcc0;
    --tail-red: #b3262c;
    --page: #ffffff;
  }
  html, body {
    margin: 0;
    padding: 0;
    width: 1200px;
    height: 1200px;
    overflow: hidden;
    background: var(--page);
  }
  .wrap-sheet {
    display: block;
    width: 1200px;
    height: 1200px;
    font-family: "Montserrat", sans-serif;
  }
  .fill-blue { fill: var(--wrap-blue); }
  .fill-green { fill: var(--wrap-green); }
  .fill-orange { fill: var(--wrap-orange); }
  .fill-white { fill: var(--wrap-white); }
  .fill-trim { fill: var(--trim-black); }
  .fill-glass { fill: var(--glass); }
  .fill-glass-light { fill: var(--glass-light); }
  .fill-hub { fill: var(--hub); }
  .fill-tail { fill: var(--tail-red); }
  .brand-name { font-weight: 700; fill: var(--wrap-blue-deep); }
  .contact-phone { font-weight: 700; fill: var(--wrap-blue-deep); }
  .contact-web { font-weight: 600; fill: var(--wrap-orange); }
  .contact-light { font-weight: 700; fill: #ffffff; }
</style>
</head>
<body>
<svg class="wrap-sheet" viewBox="0 0 1200 1200" xmlns="http://www.w3.org/2000/svg">
  <defs>
    <clipPath id="side-body">
      <path d="M22,470 L24,395 Q30,330 80,310 L250,262 Q370,170 460,130 Q520,102 600,100 L1110,98 Q1150,100 1160,140 L1172,430 L1182,470 L1150,475 L22,480 Z"/>
    </clipPath>
    <clipPath id="front-body">
      <path d="M160,620 Q330,605 500,620 Q540,640 560,740 L585,820 L585,1080 L80,1080 L80,820 L105,740 Q125,640 160,620 Z"/>
    </clipPath>
    <clipPath id="rear-body">
      <path d="M690,610 Q890,596 1070,610 Q1105,640 1115,740 L1130,870 L1130,1010 L630,1010 L630,870 L645,740 Q655,640 690,610 Z"/>
    </clipPath>
  </defs>

  <!-- Side elevation -->
  <g class="side-view">
    <g clip-path="url(#side-body)">
      <rect class="fill-white" x="0" y="90" width="1200" height="400"/>
      <path class="fill-green" d="M0,90 L820,90 L745,285 Q735,312 700,315 L300,330 Q245,334 228,380 L215,420 L0,420 Z"/>
      <path class="fill-blue" d="M0,90 L798,90 L728,278 Q720,300 690,302 L300,318 Q236,322 218,372 L206,420 L0,420 Z"/>
      <path class="fill-orange" d="M730,490 L770,400 Q785,375 830,372 L1200,345 L1200,490 Z"/>
      <rect class="fill-trim" x="0" y="458" width="1200" height="40"/>
      <path class="fill-trim" d="M0,400 L120,400 Q150,440 150,480 L0,480 Z"/>
      <path class="fill-trim" d="M1090,380 L1200,380 L1200,480 L1085,480 Z"/>
      <path class="fill-trim" d="M352,448 Q356,438 378,437 L860,428 Q868,438 860,450 L362,458 Z"/>
    </g>
    <path class="fill-glass" d="M258,310 L370,212 Q420,180 440,175 L448,300 Z"/>
    <path class="fill-glass-light" d="M348,300 L350,230 Q360,200 420,175 L600,160 Q615,162 615,180 L612,290 Z"/>
    <path class="fill-glass" d="M1118,130 L1140,130 L1152,330 L1130,330 Z"/>
    <path class="fill-tail" d="M1140,200 L1158,200 L1165,340 L1145,345 Z"/>
    <rect class="fill-trim" x="530" y="322" width="60" height="10" rx="5"/>
    <rect class="fill-trim" x="640" y="315" width="60" height="10" rx="5"/>
    <circle class="fill-trim" cx="220" cy="480" r="82"/>
    <circle class="fill-hub" cx="220" cy="480" r="54"/>
    <circle class="fill-trim" cx="995" cy="482" r="82"/>
    <circle class="fill-hub" cx="995" cy="482" r="54"/>
    <text class="contact-phone" x="350" y="388" font-size="30" transform="rotate(-2 350 388)">1-800-555-0142</text>
    <text class="contact-web" x="350" y="414" font-size="18" transform="rotate(-2 350 414)">www.732ridgeworks.com</text>
    <text class="brand-name" x="632" y="362" font-size="50" textLength="468" lengthAdjust="spacingAndGlyphs" transform="rotate(-2 632 362)">732RIDGEWORKS</text>
  </g>

  <!-- Front elevation -->
  <g class="front-view">
    <g clip-path="url(#front-body)">
      <rect class="fill-blue" x="60" y="600" width="540" height="500"/>
      <path class="fill-green" d="M165,780 L500,780 L445,900 L215,900 Z"/>
      <path class="fill-white" d="M178,780 L487,780 L437,895 L222,895 Z"/>
      <rect class="fill-trim" x="60" y="895" width="540" height="200"/>
    </g>
    <path class="fill-glass" d="M150,655 Q330,640 510,655 L530,782 L132,782 Z"/>
    <path class="fill-glass-light" d="M225,668 L295,668 L298,740 L225,740 Z"/>
    <path class="fill-glass-light" d="M345,668 L418,668 L418,740 L340,740 Z"/>
    <rect class="fill-trim" x="62" y="755" width="50" height="45" rx="10"/>
    <rect class="fill-trim" x="543" y="755" width="50" height="45" rx="10"/>
    <path class="fill-glass-light" d="M100,830 L180,865 L185,900 L108,880 Z"/>
    <path class="fill-glass-light" d="M560,830 L480,865 L475,900 L552,880 Z"/>
    <rect class="fill-glass" x="175" y="905" width="310" height="70" rx="20"/>
    <text class="brand-name" x="330" y="838" font-size="16" text-anchor="middle">732RIDGEWORKS</text>
  </g>

  <!-- Rear elevation -->
  <g class="rear-view">
    <g clip-path="url(#rear-body)">
      <rect class="fill-white" x="620" y="590" width="520" height="430"/>
      <path class="fill-green" d="M700,600 L1060,600 L1050,640 Q1048,648 1040,648 L720,648 Q712,648 710,640 Z"/>
      <path class="fill-blue" d="M705,600 L1055,600 L1046,632 Q1044,638 1036,638 L724,638 Q716,638 714,632 Z"/>
      <rect class="fill-orange" x="620" y="878" width="520" height="110"/>
      <rect class="fill-trim" x="620" y="985" width="520" height="40"/>
    </g>
    <path class="fill-tail" d="M645,720 L668,715 L668,880 L640,880 Z"/>
    <path class="fill-tail" d="M1115,720 L1092,715 L1092,880 L1120,880 Z"/>
    <line x1="880" y1="605" x2="880" y2="985" stroke="#cfcfcf" stroke-width="2"/>
    <rect class="fill-trim" x="915" y="822" width="70" height="12" rx="6"/>
    <rect class="fill-trim" x="685" y="880" width="175" height="18" rx="6"/>
    <rect class="fill-trim" x="632" y="1010" width="70" height="95" rx="12"/>
    <rect class="fill-trim" x="1058" y="1010" width="70" height="95" rx="12"/>
    <text class="brand-name" x="880" y="806" font-size="36" text-anchor="middle">732RIDGEWORKS</text>
    <text class="contact-light" x="1075" y="935" font-size="22" text-anchor="end">1-800-555-0142</text>
    <text class="contact-light" x="1075" y="958" font-size="14" text-anchor="end">www.732ridgeworks.com</text>
  </g>
</svg>
</body>
</html>
```